Casa Brisa Villa Offer

I need a flyer that i can use at different venues that offers the same thing - a complimentary stay in the Linden Feast company owned Casa Brisa Villa for 4 nights and 5 days. I need a template of a design that i can modify so it's venue specific. For example, i want it to say: "Confirm your reservation at XXXXXXX venue alongside the Linden Feast and receive a complimentary stay in the Linden Feast's company owned villa for 4 nights and 5 days! Daily cleaning, shopping and cooking is included."

Target Market(s)

Wedding Clients for our catering company at different off site wedding venues.

Industry/Entity Type

Wedding

Font styles to use
Serif

Colors

Designer to choose colors to be used in the design.

Requirements
Must have
• Linden Feast Logo
• Stylized Photos of the condo and puerto vallarta in general
Nice to have
• The Linden Feast is the Highest Rated Caterer in California on RAVO
• The Linden Feast offers turn key discounted all inclusive wedding vendor packages

```html
<!DOCTYPE html>
<html lang="en">
<head>
<meta charset="utf-8">
<title>The Linden Feast – Casa Brisa Villa Offer</title>
<link rel="stylesheet" href="https://fonts.googleapis.com/css2?family=Cinzel:wght@400&family=Encode+Sans+Condensed:wght@300;400&family=Open+Sans:ital,wght@1,400&display=swap">
<style>
  :root {
    --backdrop: #d4d4d4;
    --navy-deep: #121720;
    --navy: #1d2836;
    --slate: #2c3646;
    --steel: #34475c;
    --silver-light: #e6e8ec;
    --silver-dark: #8d939c;
    --ink-light: #ffffff;
    --pool: #3a9ad4;
    --foliage: #4f7a3a;
    --sky: #6fb3e8;
    --room-red: #a8302c;
    --room-grey: #8a8480;
  }
  * { margin: 0; padding: 0; box-sizing: border-box; }
  html, body { width: 1200px; height: 818px; overflow: hidden; background: var(--backdrop); }
  .stage { position: relative; width: 1200px; height: 818px; }

  .banner {
    position: absolute; top: 52px; width: 302px; height: 726px;
    overflow: hidden; background: var(--navy);
    box-shadow: 0 2px 6px rgba(0,0,0,.25);
  }
  .banner--front { left: 254px; }
  .banner--offer { left: 655px; }
  .banner svg.art { position: absolute; inset: 0; width: 302px; height: 726px; }

  .brand { position: absolute; left: 0; width: 302px; text-align: center; color: var(--ink-light); font-family: "Cinzel", serif; }
  .brand__name { font-size: 25px; line-height: 1; letter-spacing: .5px; white-space: nowrap; }
  .brand__tagline {
    font-size: 12.5px; line-height: 17px; letter-spacing: 11px; margin-top: 16px;
    padding-left: 11px; text-transform: uppercase;
  }

  .banner--front .brand { top: 522px; }
  .banner--offer .brand { top: 108px; }

  .web-address {
    position: absolute; left: 0; bottom: 16px; width: 302px; text-align: center;
    font-family: "Open Sans", sans-serif; font-style: italic; font-size: 14px;
    letter-spacing: 2.6px; color: var(--ink-light);
  }

  .offer {
    position: absolute; left: 26px; top: 414px; width: 257px;
    color: var(--ink-light); font-family: "Encode Sans Condensed", sans-serif; font-weight: 300;
  }
  .offer__headline { font-size: 23px; line-height: 28px; font-weight: 400; white-space: nowrap; }
  .offer__venue { font-size: 24px; line-height: 28px; letter-spacing: 4px; margin-left: 100px; margin-top: 2px; }
  .offer__body { font-size: 13.6px; line-height: 18.8px; text-align: justify; text-indent: 34px; margin-top: 2px; }
</style>
</head>
<body>
<main class="stage">

  <section class="banner banner--front">
    <svg class="art" viewBox="0 0 302 726" aria-hidden="false">
      <defs>
        <linearGradient id="frontBg" x1="0" y1="0" x2="0" y2="1">
          <stop offset="0" stop-color="#3a4452"/>
          <stop offset=".5" stop-color="#232b37"/>
          <stop offset="1" stop-color="#161b25"/>
        </linearGradient>
        <linearGradient id="resortPhoto" x1="0" y1="0" x2="0" y2="1">
          <stop offset="0" stop-color="var(--sky)"/>
          <stop offset=".35" stop-color="#c9d3c8"/>
          <stop offset=".6" stop-color="var(--foliage)"/>
          <stop offset="1" stop-color="var(--pool)"/>
        </linearGradient>
        <linearGradient id="silverEdge" x1="0" y1="0" x2="1" y2="0">
          <stop offset="0" stop-color="var(--silver-dark)"/>
          <stop offset=".5" stop-color="var(--silver-light)"/>
          <stop offset="1" stop-color="var(--silver-dark)"/>
        </linearGradient>
      </defs>
      <rect class="terrace-photo" width="302" height="726" fill="url(#frontBg)" role="img" aria-label="Dimmed photo of a villa terrace with plants and patio table"/>
      <polygon class="silver-chevron" points="0,326 151,392 302,326 302,334 151,400 0,334" fill="url(#silverEdge)"/>
      <polygon class="resort-photo" points="0,0 302,0 302,326 151,392 0,326" fill="url(#resortPhoto)" role="img" aria-label="Photo of white hillside villa with palm trees and a blue swimming pool"/>
      <polygon class="footer-chevron" points="0,691 151,626 302,691 302,726 0,726" fill="var(--navy-deep)"/>
    </svg>
    <div class="brand">
      <div class="brand__name">The Linden Feast</div>
      <div class="brand__tagline">Catering &amp;<br>Event Design</div>
    </div>
    <div class="web-address">www.thelindenfeast.com</div>
  </section>

  <section class="banner banner--offer">
    <svg class="art" viewBox="0 0 302 726">
      <defs>
        <linearGradient id="offerBg" x1="0" y1="0" x2="0" y2="1">
          <stop offset="0" stop-color="#2a3a4c"/>
          <stop offset=".6" stop-color="#1f2d3c"/>
          <stop offset="1" stop-color="#18222e"/>
        </linearGradient>
        <linearGradient id="bedroomPhoto" x1="0" y1="0" x2="1" y2="1">
          <stop offset="0" stop-color="#3c4454"/>
          <stop offset=".5" stop-color="#5a5f6c"/>
          <stop offset="1" stop-color="#2a2f3a"/>
        </linearGradient>
        <linearGradient id="terracePhoto" x1="0" y1="0" x2="1" y2="1">
          <stop offset="0" stop-color="#d8d6cf"/>
          <stop offset=".6" stop-color="var(--room-grey)"/>
          <stop offset="1" stop-color="#5b4a44"/>
        </linearGradient>
        <linearGradient id="livingPhoto" x1="0" y1="0" x2="1" y2="1">
          <stop offset="0" stop-color="var(--room-red)"/>
          <stop offset=".5" stop-color="#9a8a80"/>
          <stop offset="1" stop-color="#5e5854"/>
        </linearGradient>
        <linearGradient id="silverEdge2" x1="0" y1="0" x2="1" y2="0">
          <stop offset="0" stop-color="var(--silver-dark)"/>
          <stop offset=".5" stop-color="var(--silver-light)"/>
          <stop offset="1" stop-color="var(--silver-dark)"/>
        </linearGradient>
      </defs>
      <rect class="lounge-photo" width="302" height="726" fill="url(#offerBg)" role="img" aria-label="Dimmed photo of a villa lounge overlooking the bay"/>
      <polygon class="terrace-photo" points="0,166 151,234 151,345 0,267" fill="url(#terracePhoto)" role="img" aria-label="Photo of an open terrace lounge with red sofa"/>
      <polygon class="living-photo" points="151,234 302,166 302,267 151,345" fill="url(#livingPhoto)" role="img" aria-label="Photo of a living room with red accent wall and a red vase"/>
      <line x1="151" y1="234" x2="151" y2="345" stroke="var(--silver-light)" stroke-width="1"/>
      <polygon class="silver-chevron" points="0,166 151,234 302,166 302,172 151,240 0,172" fill="url(#silverEdge2)"/>
      <polygon class="bedroom-photo" points="0,0 302,0 302,166 151,234 0,166" fill="url(#bedroomPhoto)" role="img" aria-label="Dim photo of a villa bedroom with bedside lamps"/>
      <polygon class="footer-chevron" points="0,691 151,626 302,691 302,726 0,726" fill="var(--navy-deep)"/>
    </svg>
    <div class="brand">
      <div class="brand__name">The Linden Feast</div>
      <div class="brand__tagline">Catering &amp;<br>Event Design</div>
    </div>
    <div class="offer">
      <p class="offer__headline">Confirm your reservation at</p>
      <p class="offer__venue">XXXXXXX</p>
      <p class="offer__body">venue along side the Linden Feast and receive a complimentary stay in the Linden Feast's company owned villa for 4 nights and 5 days! Daily cleaning, shopping and cooking is included</p>
    </div>
    <div class="web-address">www.thelindenfeast.com</div>
  </section>

</main>
</body>
</html>
```